11月下旬に国立大学にて講演会をすることになりました。
その際のチラシのデザインの作成をお願いしたいです。

入れる内容は決まっておりますので、デザインを作っていただきたいです。

■チラシの使用用途
告知(データベースがメイン)
メルマガで流す
ホームページ掲載

今の所、こちらを検討しておりますので
それによってサイズを合わせていただければと思います。

ご不明点・ご質問などございましたら、お問い合わせください。
添付資料のWordデータをご確認ください。
基本はA4かA3で検討しておりますが、どちらのサイズでもできるようにして欲しいです。
片面
青系、水色系、配色は、健康系なのでシックだけど明るい感じがいいです
• 高解像度JPG (.jpg)
• イラストレーター形式 (.ai)
• PNG形式 (.png)
【追加依頼】です。

大学の教授の部分ですが、
少し自己紹介を追加することになりました。

180-200文字程度の情報を追加していただきたいので、
そこの部分の空間の確保をお願いします。
チラシの作成していただきまして、あ理がとうございます。

先方に確認をとりまして、作成していただいたチラシに
以下の情報を追加して作成していただけますでしょうか?

---------------------------------------
高森 悠介
国立大学法人翠峰大学環境共生学部
ウェルネス研究分野 教授 医学博士
ハーウッド大学客員教授
全米ビジネス書ベストセラー『The Quiet Harbor(クワイエットハーバー) 2nd edition世界の100 歳人に学ぶ健康と長寿9つのルール』(2022年、緑陽舎)翻訳・監修者。
ウェルネス研究、ウェルネスツーリズム研究の第一人者。海洋療法学者。

よろしくお願いします。

国立大学での講義という点で清潔感があり、スタイリッシュなデザインから見やすさ、分かりやすさなどからこちらのデザインにさせていただきました。

たくさんの方にご応募・ご協力いただきまして、ありがとうございました。

```html
<!DOCTYPE html>
<html lang="ja">
<head>
<meta charset="utf-8">
<title>腰痛テンプレート施術 公開講座</title>
<link href="https://fonts.googleapis.com/css2?family=Noto+Sans+JP:wght@400;500;700;900&family=Montserrat:wght@600;700;800&display=swap" rel="stylesheet">
<style>
:root{
  --blue:#1e78c8;
  --blue-dark:#0f4f91;
  --sky:#e8f3fb;
  --sky-mid:#b9d9ef;
  --ink:#2b3440;
  --muted:#5d6a78;
  --white:#ffffff;
}
*{box-sizing:border-box;margin:0;padding:0}
html,body{width:847px;height:1200px;overflow:hidden;background:var(--white)}
body{font-family:"Noto Sans JP",sans-serif;color:var(--ink);position:relative}
.photo{position:absolute;background:linear-gradient(135deg,#c9dcea,#8fb1ca 60%,#6f93ad)}
.hero-photo{left:607px;top:0;width:240px;height:300px;background:linear-gradient(160deg,#dfe9f1,#9fbcd2 55%,#46627c)}
.p1{left:607px;top:306px;width:240px;height:150px}
.p2{left:607px;top:462px;width:118px;height:140px;background:linear-gradient(135deg,#e4edf4,#a9c3d6)}
.p3{left:729px;top:462px;width:118px;height:140px;background:linear-gradient(135deg,#a6c2d6,#5a7d98)}
.p4{left:607px;top:608px;width:240px;height:170px;background:linear-gradient(135deg,#d5e3ee,#7f9fb8)}
.p5{left:607px;top:784px;width:240px;height:150px;background:linear-gradient(135deg,#bcd2e2,#6c8ca6)}
.p6{left:607px;top:940px;width:118px;height:130px;background:linear-gradient(135deg,#e1ebf2,#98b5ca)}
.p7{left:729px;top:940px;width:118px;height:130px;background:linear-gradient(135deg,#9dbad0,#557890)}
.p8{left:607px;top:1076px;width:240px;height:124px;background:linear-gradient(135deg,#cfdfeb,#86a6bf)}

.column{position:absolute;left:28px;top:22px;width:566px;height:1120px;display:flex;flex-direction:column}
.head{padding-left:8px}
.badge{display:inline-block;background:var(--blue);color:var(--white);font-weight:700;font-size:19px;padding:5px 18px;border-radius:20px;letter-spacing:.05em}
.cohost{margin-top:12px;font-size:17px;font-weight:700;color:var(--blue-dark)}
.title{margin-top:8px;font-size:53px;line-height:1.16;font-weight:900;color:var(--blue);letter-spacing:.02em}
.date{margin-top:14px;display:flex;align-items:center;gap:14px}
.label{flex:none;background:var(--blue-dark);color:var(--white);font-size:15px;font-weight:700;padding:4px 10px;border-radius:3px;line-height:1.3}
.date-main{font-family:"Montserrat",sans-serif;font-weight:800;font-size:52px;color:var(--blue-dark);line-height:1}
.date-main small{font-family:"Noto Sans JP",sans-serif;font-size:24px;font-weight:700}
.time{margin:4px 0 0 64px;font-family:"Montserrat",sans-serif;font-weight:700;font-size:22px;color:var(--blue-dark)}
.venue{margin-top:12px;display:flex;gap:14px;align-items:flex-start}
.venue-text{font-weight:700;font-size:16px;line-height:1.5;color:var(--ink)}

.section{margin-top:22px}
.section.overview{margin-top:26px}
.sec-title{background:var(--blue);color:var(--white);font-size:14px;font-weight:700;padding:4px 12px;display:inline-block}
.sec-rule{border-top:2px solid var(--blue);margin-top:-1px}
.overview p{margin-top:10px;font-size:12px;line-height:1.8;color:var(--ink)}
.person{display:flex;gap:16px;margin-top:10px;align-items:flex-start}
.person-text{flex:1;font-size:11.5px;line-height:1.7}
.person-text b{font-size:15px;display:block;margin-bottom:2px}
.avatar{width:72px;height:72px;border-radius:50%;background:linear-gradient(135deg,var(--sky-mid),#7ea6c6);flex:none;margin-top:6px}

.footer{margin-top:24px;border-top:1px solid var(--sky-mid);padding-top:18px}
.brand{display:flex;align-items:center;gap:10px;font-size:26px;font-weight:700;color:var(--blue-dark)}
.brand i{width:22px;height:22px;background:var(--blue);display:block}
.company{margin-top:10px;font-size:16px;font-weight:700}
.contact{margin-top:8px;font-size:12.5px;line-height:1.8;color:var(--muted)}
.band{position:absolute;left:0;top:1150px;width:607px;height:50px;background:var(--sky)}
</style>
</head>
<body>
  <div class="photo hero-photo" role="img" aria-label="講師が受講者に施術を実演している写真"></div>
  <div class="photo p1" role="img" aria-label="講義会場で話す講師の写真"></div>
  <div class="photo p2" role="img" aria-label="施術の実技練習の写真"></div>
  <div class="photo p3" role="img" aria-label="腰部への施術の写真"></div>
  <div class="photo p4" role="img" aria-label="受講者で埋まる講義室の写真"></div>
  <div class="photo p5" role="img" aria-label="ベッド上での施術指導の写真"></div>
  <div class="photo p6" role="img" aria-label="実技を見守る受講者の写真"></div>
  <div class="photo p7" role="img" aria-label="背中への手技の写真"></div>
  <div class="photo p8" role="img" aria-label="集合した受講者の写真"></div>

  <main class="column">
    <header class="head">
      <span class="badge">100名先着講座無料！</span>
      <p class="cohost">翠峰大学環境共生学部ウェルネス研究分野 共催</p>
      <h1 class="title">腰痛テンプレート<br>施術 公開講座</h1>
      <div class="date">
        <span class="label">日時</span>
        <span class="date-main">11.23<small>（木/祝）</small></span>
      </div>
      <p class="time">10:30 ~ 17:00</p>
      <div class="venue">
        <span class="label">会場</span>
        <p class="venue-text">国立大学法人翠峰大学 環境講義棟 215 教室<br>翠峰県緑川郡若葉町字森原 1 番地</p>
      </div>
    </header>

    <section class="section overview">
      <span class="sec-title">公開概要</span>
      <div class="sec-rule"></div>
      <p>腰痛は多くの人が抱える身近な悩みです。本講座では、現場で再現しやすい腰痛テンプレート施術を、講義と実技を通して分かりやすく学びます。評価の流れから手技の組み立て方、セルフケア指導のポイントまでを一日で体系的に身につけることができます。施術者の方はもちろん、ウェルネスや健康づくりに関心のある方もぜひご参加ください。先着100名様まで受講料は無料です。</p>
    </section>

    <section class="section profile">
      <span class="sec-title">講師プロフィール</span>
      <div class="sec-rule"></div>
      <div class="person">
        <div class="person-text">
          <b>高森 悠介</b>
          国立大学法人翠峰大学環境共生学部 ウェルネス研究分野 教授 医学博士／ハーウッド大学客員教授。全米ビジネス書ベストセラー『The Quiet Harbor（クワイエットハーバー）2nd edition 森に暮らす人々が教える心と体を整える7つの習慣』（2022年、緑陽舎）翻訳・監修者。ウェルネス研究、ウェルネスツーリズム研究の第一人者。海洋療法学者。
        </div>
        <div class="avatar" role="img" aria-label="講師の顔写真"></div>
      </div>
    </section>

    <section class="section facil">
      <span class="sec-title">ファシリテーター</span>
      <div class="sec-rule"></div>
      <div class="person">
        <div class="person-text">
          <b>ファシリテーター</b>
          施術院での臨床経験をもとに、実技パートの進行とサポートを担当します。受講者一人ひとりの手技を確認しながら、現場ですぐに活かせるコツを丁寧にお伝えします。
        </div>
        <div class="avatar" role="img" aria-label="ファシリテーターの顔写真"></div>
      </div>
    </section>

    <footer class="footer">
      <div class="brand"><i></i>Health Leaf Press</div>
      <p class="company">株式会社ヘルスリーフ出版</p>
      <p class="contact">事前登録が必要です。下記メールアドレスよりご登録ください。<br>定員：100名先着順（定員になり次第締め切り）<br>お問い合わせ：info@healthleafpress.example</p>
    </footer>
  </main>
  <div class="band"></div>
</body>
</html>
```